verdant terraces simple classy business card design

my name is owen harlow and I run a gardening business aimed at high class verdant terraces. the business name is verdant terraces and our logo was designed on pixel forum .My clientel are anything from residential homes to businesses. I take pride in my work and know that I offer a service like no other in my area.
The business card will be used to represent my business and I want it to be not only rememberable, but simplistic and modern. Eye catching too. Of course I would like it relatable to gardening and appealing to the correct clientel - those being garden enthusiasts, prestigious homes and businesses that are after top of the line gardening services like no other on the market.
I am not a typical lawn mowing business so I don't want a typical card design that represents that. The gardens I work with are generally million dollar properties with owners who are very garden proud looking for upkeep and guidance from me along with sometimes whole new garden designs. I want the business cards to show to my clients that I take pride, as they do, in their garden. And I want them to know from my card that I am a professional, qualified horticulturist offering them a top of the line service for life. I want them to refer my business on. I want them to look at my business card and see class and professionalism in a modern unique bold way.
The card should be simple with the possibility of the logo on the front being embossed/debossed and my details on the back the card should have a organic garden feel it's very important to me that it is absolutely perfect
I am also very open to ideas and suggestions so look forward to seeing the designs. the business logo has been supplied with this project and I want the card to be double sided

Contact info is
Owen Harlow - Managing Director / Horticulturist
Phone : 0481 526 704
Email: owenharlow@verdantterraces.com.au

Target Market(s)

high class gardens residential and commercial

Industry/Entity Type

Gardener

Contact Information for Business Card

Contact info is
Phone : 0481 526 704

PLEASE MAKE CARD DOUBLE SIDED

Requirements
Must have
• organic simple classy modern feel
• must flow with the current logo that has been supplied with this project
• Double sided
• Must explain in a simple way that I deal with high end gardens and I'm a qualified horticulturist
Nice to have
• embossed debossed logo
Should not have
• shouldn't be to busy or cheap looking

```html
<!DOCTYPE html>
<html lang="en">
<head>
<meta charset="utf-8">
<title>Verdant Terraces – Business Card</title>
<link href="https://fonts.googleapis.com/css2?family=Source+Sans+3:wght@400;600&display=swap" rel="stylesheet">
<style>
  :root {
    --leaf-green: #5f9b50;
    --leaf-green-light: #8fbf7e;
    --card-white: #ffffff;
    --backdrop: #ecebe8;
    --card-shadow: rgba(0, 0, 0, 0.18);
  }
  * { margin: 0; padding: 0; box-sizing: border-box; }
  html, body {
    width: 1200px;
    height: 900px;
    overflow: hidden;
    background: var(--backdrop);
    font-family: "Source Sans 3", "Myriad Pro", Arial, sans-serif;
  }
  .canvas {
    position: relative;
    width: 1200px;
    height: 900px;
  }
  .card {
    position: absolute;
    box-shadow: 0 6px 18px var(--card-shadow);
    overflow: hidden;
  }

  /* Front: details side */
  .card--details {
    left: 238px;
    top: 62px;
    width: 555px;
    height: 342px;
    background: var(--leaf-green);
    color: var(--card-white);
  }
  .card--details .text-block {
    position: absolute;
    z-index: 2;
    white-space: nowrap;
  }
  .holder-name {
    left: 38px;
    top: 36px;
    font-size: 19px;
    font-weight: 600;
    line-height: 1.2;
  }
  .holder-role {
    left: 38px;
    top: 60px;
    font-size: 15px;
    font-weight: 400;
  }
  .address {
    left: 38px;
    top: 190px;
    font-size: 15px;
    line-height: 21px;
  }
  .contact-list {
    left: 38px;
    top: 245px;
    list-style: none;
    font-size: 15px;
    line-height: 20px;
  }
  .contact-list li {
    display: flex;
    align-items: center;
    gap: 8px;
  }
  .contact-icon {
    width: 11px;
    height: 11px;
    fill: var(--card-white);
    flex: none;
  }
  .tree-illustration {
    position: absolute;
    z-index: 1;
    left: 280px;
    top: 0;
    width: 275px;
    height: 342px;
    background:
      radial-gradient(circle at 58% 36%, var(--leaf-green-light) 0 34%, transparent 35%),
      linear-gradient(90deg, var(--leaf-green) 0 40%, var(--card-white) 60%);
  }

  /* Back: brand side */
  .card--brand {
    left: 457px;
    top: 518px;
    width: 560px;
    height: 343px;
    background: var(--card-white);
  }
  .brand-mark {
    position: absolute;
    left: 50%;
    top: 104px;
    width: 82px;
    height: 82px;
    margin-left: -41px;
    border-radius: 50%;
    background: var(--leaf-green);
  }
  .brand-name {
    position: absolute;
    left: 0;
    right: 0;
    top: 192px;
    text-align: center;
    color: var(--leaf-green);
    font-size: 34px;
    font-weight: 400;
    letter-spacing: 3px;
    line-height: 1.1;
    text-transform: uppercase;
  }
</style>
</head>
<body>
  <main class="canvas">
    <section class="card card--details" aria-label="Card front with contact details">
      <h1 class="text-block holder-name">Owen Harlow</h1>
      <p class="text-block holder-role">Managing Director / Horticulturist</p>
      <p class="text-block address">12345, Address Goes Here<br>Country Name, 123456.</p>
      <ul class="text-block contact-list">
        <li>
          <svg class="contact-icon" viewBox="0 0 24 24" aria-hidden="true"><path d="M6.6 10.8a15 15 0 0 0 6.6 6.6l2.2-2.2c.3-.3.7-.4 1-.2 1.1.4 2.3.6 3.6.6.6 0 1 .4 1 1V20c0 .6-.4 1-1 1C10.6 21 3 13.4 3 4c0-.6.4-1 1-1h3.5c.6 0 1 .4 1 1 0 1.3.2 2.5.6 3.6.1.3 0 .7-.2 1z"/></svg>
          0481 526 704
        </li>
        <li>
          <svg class="contact-icon" viewBox="0 0 24 24" aria-hidden="true"><path d="M2 5h20v14H2z M2 5l10 8 10-8" /></svg>
          owenharlow@verdantterraces.com.au
        </li>
        <li>
          <svg class="contact-icon" viewBox="0 0 24 24" aria-hidden="true"><circle cx="12" cy="12" r="10"/></svg>
          www.verdantterraces.com.au
        </li>
      </ul>
      <div class="tree-illustration" role="img" aria-label="Large white leafy tree illustration on green"></div>
    </section>

    <section class="card card--brand" aria-label="Card back with business name">
      <div class="brand-mark" aria-hidden="true"></div>
      <p class="brand-name">Verdant Terraces</p>
    </section>
  </main>
</body>
</html>
```